Business Card for Pet Food Deliver

Looking for a business card design for a start up company. We are Brisk Hound, Premium Pet Products Brought Round.

We market and are designing a website where our clients can go to and order pet food. We then deliver to a local client base. We do person to person deliver, we do not ship at this point. We are starting off with dog and cat food and treats.

Attached is our logo. We are looking for a fun yet professional design. Eye catching with color but not over the top with color. Looking for a double sided card. Contact info on the front and our logo on the back maybe. . .

I am a huge green fan. However, I am thinking I like the orange a bit more then the blue and green for dominant colors. . .

I am attaching our logo.

The file that has our slogan under has a minor change not implemented yet. The word 'Premium' should be gray to match and the word 'Delivered' should be black to match.

Target Market(s)

We are looking to service those pet owners looking for the convenience of not having to drive to a pet store to purchase their products. We are looking for those who are web savvy and purchase online.

We will also be targeting seniors in senior communities without consistent transprotation.

Industry/Entity Type

Pet

Font styles to use
Sans Serif

Colors
f37122
3176b5
acd036

Requirements
Must have
• Double sided. Logo only on one side with a bold color for the background.

Space for name, phone number, website address, mailing address.
Should not have
• No paws, delivery trucks.

```html
<!DOCTYPE html>
<html lang="en">
<head>
<meta charset="utf-8">
<title>Brisk Hound – Business Card</title>
<link rel="stylesheet" href="https://fonts.googleapis.com/css2?family=Arimo:wght@400;700&family=Open+Sans:ital,wght@0,400;1,700&display=swap">
<style>
  :root {
    --orange: #f37122;
    --blue: #2b77b5;
    --green: #acd036;
    --grey: #6d6e71;
    --white: #ffffff;
    --page: #ffffff;
  }
  * { margin: 0; padding: 0; box-sizing: border-box; }
  html, body {
    width: 1200px; height: 792px; overflow: hidden;
    background: var(--page);
  }
  .canvas { position: relative; width: 1200px; height: 792px; }

  .card {
    position: absolute;
    border-radius: 14px;
    overflow: hidden;
  }
  .card svg { position: absolute; inset: 0; display: block; }

  /* Logo side */
  .card--logo { left: 85px; top: 66px; width: 461px; height: 280px; background: var(--green); }
  .brand {
    position: absolute; left: 0; width: 100%; top: 112px;
    text-align: center;
    font-family: "Open Sans", sans-serif;
    font-weight: 400; font-size: 46px; letter-spacing: -0.5px;
    color: var(--grey);
    line-height: 1;
  }
  .tagline {
    position: absolute; left: 0; width: 100%; top: 170px;
    text-align: center;
    font-family: "Open Sans", sans-serif;
    font-style: italic; font-weight: 700; font-size: 9.5px;
    color: var(--grey);
    letter-spacing: 0.2px;
  }

  /* Contact side */
  .card--contact { left: 659px; top: 459px; width: 463px; height: 276px; background: var(--orange); }
  .person {
    position: absolute; right: 32px; top: 32px; text-align: right;
    color: var(--white); font-family: "Arimo", sans-serif;
  }
  .person__name { font-weight: 700; font-size: 21px; letter-spacing: -0.3px; line-height: 1.1; }
  .person__role { font-size: 10px; margin-top: 1px; margin-right: 10px; }
  .contact-list {
    position: absolute; left: 48px; top: 145px; list-style: none;
    color: var(--white); font-family: "Open Sans", sans-serif; font-size: 12.5px;
  }
  .contact-list li { height: 25px; line-height: 25px; white-space: pre; }
</style>
</head>
<body>
<main class="canvas">

  <section class="card card--logo" aria-label="Business card, logo side">
    <svg width="461" height="280" viewBox="0 0 461 280" aria-hidden="true">
      <polygon points="0,210 187,210 221,229 255,210 461,210 461,218 257,218 221,238 185,218 0,218" fill="var(--blue)"/>
      <polygon points="0,229 221,245 461,229 461,236 0,236" fill="var(--white)"/>
      <polygon points="0,236 190,236 221,258 252,236 461,236 461,280 0,280" fill="var(--orange)"/>
      <polygon points="0,228 192,228 221,246 250,228 461,228 461,236 252,236 221,258 190,236 0,236" fill="var(--white)"/>
    </svg>
    <div class="brand">Brisk Hound</div>
    <div class="tagline">PREMIUM PET PRODUCTS BROUGHT ROUND</div>
  </section>

  <section class="card card--contact" aria-label="Business card, contact side">
    <svg width="463" height="276" viewBox="0 0 463 276" aria-hidden="true">
      <polygon points="30,0 463,0 463,276 412,276" fill="var(--green)"/>
      <polygon points="105,20 452,0 463,0 463,276 434,276" fill="var(--blue)"/>
    </svg>
    <div class="person">
      <div class="person__name">Daniel Ferris</div>
      <div class="person__role">Nutrition Specialist</div>
    </div>
    <ul class="contact-list">
      <li>920-555-0148</li>
      <li>briskhound@mail.com</li>
      <li>www.BriskHoundDelivers.com</li>
      <li>2280 Orchard Lane  Fairbrook, WI 54000</li>
    </ul>
  </section>

</main>
</body>
</html>
```